【 概要 】 業界最安値のパーソナルジムを運営しています。 https://solvekara.jp/ 上記ジムのインスタ広告用のクリエイティブを募集します。 ※画像はフリー素材で問題ありません。 【 依頼内容 】 ・サイズ: 500px × 500px ・作成数: 1種類 ・利用用途:インスタ広告 【 デザインイメージ 】 ・ターゲット層:都心在住の20〜30代女性 ・雰囲気:ナチュラルでおしゃれな雰囲気 【 契約金額(税抜) 】 2000円 ※契約金額(税込)からシステム利用料を差し引いた金額が、ワーカーさまの受取金額となります その他ご質問等ありましたら、気軽にお問い合わせください。 ご応募をお待ちしております! |
弊社ジムとの相性が良く、こちらを採用致しました。
皆様、素敵なご提案ありがとうございました。また機会ございましたら、どうぞ宜しくお願い致します。

```html
<!DOCTYPE html>
<html lang="ja">
<head>
<meta charset="utf-8">
<title>Fit Lumina 広告</title>
<link rel="stylesheet" href="https://fonts.googleapis.com/css2?family=M+PLUS+1p:wght@700;800;900&family=Noto+Serif+JP:wght@600;700&family=Cormorant+Garamond:wght@500&display=swap">
<style>
  :root {
    --pink: #f5248a;
    --ink: #141414;
    --yellow: #fff22a;
    --white: #ffffff;
    --bar-dark: #0d0d0d;
  }
  * { margin: 0; padding: 0; box-sizing: border-box; }
  html, body { width: 1200px; height: 1200px; overflow: hidden; background: var(--white); }
  .ad {
    position: relative;
    width: 1200px;
    height: 1200px;
    overflow: hidden;
    font-family: "M PLUS 1p", sans-serif;
    color: var(--ink);
  }
  .photo {
    position: absolute;
    inset: 0 0 138px 0;
    background:
      radial-gradient(ellipse 420px 620px at 260px 520px, #d9b6a0 0%, #c9a28c 35%, rgba(220,200,190,0) 75%),
      radial-gradient(ellipse 380px 220px at 230px 860px, #e79ab7 0%, rgba(240,170,195,0) 80%),
      linear-gradient(100deg, #b9b3b0 0%, #eeeae8 40%, #f7f6f5 70%, #ffffff 100%);
  }
  .headline {
    position: absolute;
    right: 64px;
    top: 42px;
    font-weight: 900;
    font-size: 104px;
    line-height: 1.26;
    letter-spacing: 0.02em;
    text-align: left;
  }
  .headline .accent { color: var(--pink); }
  .headline .line { display: block; white-space: nowrap; }
  .headline .line-2 { padding-left: 8px; }
  .badge {
    position: absolute;
    border-radius: 50%;
    background: var(--yellow);
    display: flex;
    flex-direction: column;
    align-items: center;
    justify-content: center;
    font-weight: 800;
    font-size: 29px;
    line-height: 1.55;
    text-align: center;
  }
  .badge .accent { color: var(--pink); }
  .badge-price { left: 514px; top: 432px; width: 284px; height: 284px; }
  .badge-trainer { left: 798px; top: 438px; width: 310px; height: 310px; }
  .price {
    position: absolute;
    left: 456px;
    top: 838px;
    display: flex;
    align-items: flex-end;
    color: var(--pink);
    font-weight: 900;
  }
  .price .label {
    writing-mode: vertical-rl;
    font-size: 52px;
    line-height: 1;
    color: var(--ink);
    margin-right: 14px;
    margin-bottom: 16px;
    letter-spacing: 0.05em;
  }
  .price .amount { font-size: 150px; line-height: 1; letter-spacing: -0.01em; }
  .price .unit { font-size: 58px; line-height: 1; margin-left: 6px; margin-bottom: 18px; }
  .footer-bar {
    position: absolute;
    left: 0; right: 0; bottom: 0;
    height: 138px;
    display: flex;
  }
  .brand {
    width: 600px;
    background: var(--bar-dark);
    color: var(--white);
    display: flex;
    align-items: center;
    padding-left: 62px;
    gap: 26px;
  }
  .brand-dot {
    width: 62px; height: 62px;
    border-radius: 50%;
    border: 2px solid var(--white);
  }
  .brand-name {
    font-family: "Cormorant Garamond", serif;
    font-weight: 500;
    font-size: 58px;
    letter-spacing: 0.01em;
  }
  .cta {
    flex: 1;
    background: var(--pink);
    color: var(--white);
    display: flex;
    align-items: center;
    justify-content: center;
    font-family: "Noto Serif JP", serif;
    font-weight: 700;
    font-size: 60px;
    letter-spacing: 0.03em;
  }
</style>
</head>
<body>
<main class="ad">
  <div class="photo" role="img" aria-label="ワイヤレスイヤホンを着け、首にピンクのタオルをかけて窓の外を眺めるトレーニング中の女性"></div>

  <h1 class="headline">
    <span class="line line-1"><span class="accent">続</span>かない<span class="accent">ジム</span>に</span>
    <span class="line line-2">もう<span class="accent">サヨナラ♪</span></span>
  </h1>

  <div class="badge badge-price">
    <span>続けやすい</span>
    <span class="accent">業界最安値！</span>
  </div>
  <div class="badge badge-trainer">
    <span class="accent">プロトレーナー</span>
    <span>による</span>
    <span class="accent">マンツーマン指導</span>
  </div>

  <div class="price">
    <span class="label">月額</span>
    <span class="amount">16,500</span>
    <span class="unit">円〜</span>
  </div>

  <footer class="footer-bar">
    <div class="brand">
      <span class="brand-dot"></span>
      <span class="brand-name">Fit Lumina</span>
    </div>
    <div class="cta">無料体験を予約</div>
  </footer>
</main>
</body>
</html>
```